Website for new child psychology practice

New clinical psychology practice in NSW Australia, specialising in work with children, adolescents and families. I would like to feature the colours in the logo, which was recently designed by pixelmesa designer Odette.
I am seeking a professional looking page, which is easy to navigate and is colourful and playful but not childish.
Target Market(s)
Parents and professionals
Industry/Entity Type
Health
Coding
Coded - Design and coding required
Number of Pages Required
1 page
Font styles to use
Serif
Requirements
Must have
- Pages for 'About us' 'Services' 'Fees and information' 'Contact us'
Should not have
- Childish stock photos

```html
<!DOCTYPE html>
<html lang="en">
<head>
<meta charset="utf-8">
<title>Dr Clara Bennett – Child Psychology</title>
<link rel="stylesheet" href="https://fonts.googleapis.com/css2?family=Noto+Serif:wght@400;500;600&family=Inter:wght@400;500&display=swap">
<style>
:root{
  --purple:#8e1a78;
  --purple-light:#a62b95;
  --purple-dark:#6e1360;
  --orange:#e0651e;
  --red:#cf3428;
  --ink:#1e1e1e;
  --grey:#6f6f6f;
  --line:#d9d9d9;
  --white:#fff;
}
*{box-sizing:border-box;margin:0;padding:0}
html,body{width:1200px;height:3057px;overflow:hidden}
body{position:relative;background:var(--white);font-family:"Inter",sans-serif;color:var(--ink)}
.abs{position:absolute}
.serif{font-family:"Noto Serif",serif}
.topbar{left:0;top:0;width:1200px;height:32px;background:var(--purple);color:var(--white);font-family:"Noto Serif",serif;font-size:13px}
.topbar span{position:absolute;top:8px;display:flex;align-items:center;gap:6px}
.hero{left:0;top:32px;width:1200px;height:653px;background:linear-gradient(120deg,#5b6a3c 0%,#8a8a5a 35%,#c9a28e 60%,#7a6d8d 85%,#4d5a3a 100%)}
.hero::after{content:"";position:absolute;inset:0;background:linear-gradient(90deg,rgba(0,0,0,.35),rgba(0,0,0,.05) 60%)}
.brand{display:flex;align-items:center;gap:10px;font-family:"Noto Serif",serif;font-size:24px;color:var(--purple)}
.brand i{display:block;width:26px;height:26px;border-radius:50%;background:var(--purple)}
.nav{top:63px;font-family:"Noto Serif",serif;font-size:12.5px;color:#2a2a2a;text-transform:uppercase;z-index:2}
.btn{display:flex;align-items:center;justify-content:center;background:var(--purple);color:var(--white);font-family:"Noto Serif",serif;font-size:13px;text-transform:uppercase;border-radius:3px}
.hero-title{left:121px;top:200px;font-size:56px;line-height:64px;color:var(--white);font-weight:500;z-index:2}
.hero-sub{left:121px;top:353px;width:450px;font-size:20px;line-height:24px;color:var(--white);z-index:2}
h2{font-family:"Noto Serif",serif;font-weight:400;font-size:33px;line-height:40px}
.body{font-size:17.5px;line-height:26px}
.about-frame{left:656px;top:810px;width:389px;height:434px;border-radius:12px;background:linear-gradient(180deg,var(--orange),#c95b20)}
.about-photo{left:673px;top:786px;width:387px;height:437px;background:linear-gradient(180deg,#eef0f2 0%,#d8d2c8 45%,#3f7d4c 75%,#8b8a80 100%)}
.logo-card{left:620px;top:1103px;width:328px;height:103px;background:var(--white);box-shadow:0 10px 30px rgba(0,0,0,.12);display:flex;align-items:center;justify-content:center}
.band{left:0;top:1379px;width:1200px;height:800px}
.circle-outer{left:99px;top:1464px;width:408px;height:408px;border-radius:50%;background:#ab3a9b}
.circle-inner{left:127px;top:1490px;width:356px;height:356px;border-radius:50%;background:#d9d9d9}
.kids{left:98px;top:1530px;width:450px;height:320px;border-radius:40% 40% 10px 10px;background:linear-gradient(180deg,#7a5a4a,#c8a08a 50%,#e9e3df)}
.card{width:239px;height:289px;background:var(--white);box-shadow:0 12px 30px rgba(0,0,0,.12)}
.card .img{height:196px}
.card p{position:absolute;left:24px;top:216px;font-family:"Noto Serif",serif;font-size:19px;line-height:24px;text-transform:uppercase;color:var(--ink)}
.field{border:1px solid var(--line);border-radius:3px;font-size:13px;color:#9a9a9a;padding:10px 24px;background:var(--white)}
.info{display:flex;gap:10px;font-size:14px;line-height:17px}
.footer{left:0;top:2761px;width:1200px;height:296px;background:var(--purple)}
.foot-bottom{left:0;top:3017px;width:1200px;height:40px;background:var(--purple-dark);color:#e6cbe0;font-family:"Noto Serif",serif;font-size:12.5px;display:flex;align-items:center;justify-content:center}
.foot-h{font-family:"Noto Serif",serif;font-size:15px;color:var(--white);text-transform:uppercase}
.foot-link{font-family:"Noto Serif",serif;font-size:12px;color:#f2dcec;text-transform:uppercase}
.fi{color:var(--white);font-size:13.5px}
.social{display:flex;gap:14px}
.social i{width:15px;height:15px;border-radius:50%;background:var(--white);display:block}
</style>
</head>
<body>

<div class="abs topbar">
  <span style="left:835px"><svg width="16" height="14" viewBox="0 0 16 14" fill="none" stroke="#fff" stroke-width="1.4"><rect x="1" y="1" width="14" height="12" rx="2"/><path d="M1 3l7 5 7-5"/></svg>info@clarabennett.com</span>
  <span style="left:1040px"><svg width="14" height="14" viewBox="0 0 24 24" fill="none" stroke="#fff" stroke-width="2"><path d="M22 16.9v3a2 2 0 0 1-2.2 2 19.8 19.8 0 0 1-8.6-3.1 19.5 19.5 0 0 1-6-6A19.8 19.8 0 0 1 2.1 4.2 2 2 0 0 1 4.1 2h3a2 2 0 0 1 2 1.7c.1.9.4 1.8.7 2.7a2 2 0 0 1-.5 2.1L8 9.8a16 16 0 0 0 6 6l1.3-1.3a2 2 0 0 1 2.1-.4c.9.3 1.8.6 2.7.7a2 2 0 0 1 1.7 2z"/></svg>021 555 018</span>
</div>

<div class="abs hero" role="img" aria-label="Photo of three smiling children playing together on a rope swing outdoors"></div>

<div class="abs brand" style="left:68px;top:56px;z-index:2"><i></i>Dr Clara Bennett</div>
<div class="abs nav" style="left:491px">About us</div>
<div class="abs nav" style="left:576px">Our services</div>
<div class="abs nav" style="left:694px">Fees and information</div>
<div class="abs nav" style="left:868px">Contact us</div>
<div class="abs btn" style="left:966px;top:46px;width:158px;height:49px;z-index:2">Get in touch</div>

<h1 class="abs serif hero-title">The Child Psychology<br>Service</h1>
<p class="abs serif hero-sub">Caring, therapeutic, psychological support for children and their families.</p>

<h2 class="abs" style="left:145px;top:867px">About Us</h2>
<p class="abs body" style="left:145px;top:930px;width:420px">Lorem ipsum dolor sit amet consectetur. Lacus sed orci blandit eu magna pharetra porttitor. Enim quam arcu habitasse pulvinar tincidunt. Mi lacus vitae non maecenas urna diam porttitor. Enim nec consectetur sollicitudin convallis a curabitur mattis id adipiscing.</p>
<div class="abs btn" style="left:145px;top:1099px;width:158px;height:49px">Get in touch</div>

<div class="abs about-frame"></div>
<div class="abs about-photo" role="img" aria-label="Portrait of the psychologist in a green blazer standing outdoors"></div>
<div class="abs logo-card"><div class="brand" style="font-size:23px"><i></i>Dr Clara Bennett</div></div>

<svg class="abs band" width="1200" height="800" viewBox="0 0 1200 800" preserveAspectRatio="none">
  <defs><linearGradient id="bandGrad" x1="0" y1="0" x2="0" y2="1"><stop offset="0" stop-color="#a62b95"/><stop offset="1" stop-color="#8a1572"/></linearGradient></defs>
  <polygon points="0,0 1200,93 1200,793 0,639" fill="url(#bandGrad)"/>
</svg>

<div class="abs circle-outer"></div>
<div class="abs circle-inner"></div>
<div class="abs kids" role="img" aria-label="Group of five smiling children lying together, arms folded"></div>

<h2 class="abs" style="left:565px;top:1507px;color:var(--white)">Our Services</h2>
<p class="abs body" style="left:566px;top:1569px;width:530px;color:var(--white)">Lorem ipsum dolor sit amet consectetur. Lacus sed orci blandit eu magna pharetra porttitor. Enim quam arcu habitasse pulvinar tincidunt. Mi lacus vitae non maecenas urna diam porttitor. Enim nec consectetur sollicitudin convallis a curabitur mattis id adipiscing.</p>
<div class="abs btn" style="left:566px;top:1729px;width:158px;height:49px;background:var(--red)">Get in touch</div>

<div class="abs card" style="left:88px;top:1908px"><div class="img" role="img" aria-label="Doctor giving a high five to a young patient" style="background:linear-gradient(135deg,#c9b59a,#efece6)"></div><p>Specialist<br>trauma</p></div>
<div class="abs card" style="left:350px;top:1908px"><div class="img" role="img" aria-label="Hands holding paper cut-out family figures" style="background:linear-gradient(135deg,#8f5a55,#d8a69a)"></div><p>Therapeutic<br>parenting</p></div>
<div class="abs card" style="left:610px;top:1904px"><div class="img" role="img" aria-label="Child holding an adult's hand outdoors" style="background:linear-gradient(135deg,#4d6b35,#a9b58c)"></div><p>Non-violent<br>resistance</p></div>
<div class="abs card" style="left:872px;top:1908px"><div class="img" role="img" aria-label="Therapist taking notes with a child holding a teddy bear" style="background:linear-gradient(135deg,#e8e8ea,#7fa8c8)"></div><p>Consultation</p></div>

<h2 class="abs" style="left:123px;top:2330px;font-size:40px;line-height:48px">CONTACT</h2>
<p class="abs body" style="left:129px;top:2386px;width:370px;font-size:17px">If you would like to get in touch with us, you can call us, send us a quick email or fill out our contact form and we'll get back to you as fast as we possibly can.</p>
<div class="abs" style="left:130px;top:2512px;display:flex;flex-direction:column;gap:6px">
  <div class="info"><svg width="16" height="14" viewBox="0 0 16 14" fill="none" stroke="#e0651e" stroke-width="1.4"><rect x="1" y="1" width="14" height="12" rx="2"/><path d="M1 3l7 5 7-5"/></svg>hello@brightleafcare.com</div>
  <div class="info"><svg width="16" height="14" viewBox="0 0 24 24" fill="none" stroke="#e0651e" stroke-width="2"><path d="M22 16.9v3a2 2 0 0 1-2.2 2 19.8 19.8 0 0 1-8.6-3.1 19.5 19.5 0 0 1-6-6A19.8 19.8 0 0 1 2.1 4.2 2 2 0 0 1 4.1 2h3a2 2 0 0 1 2 1.7c.1.9.4 1.8.7 2.7a2 2 0 0 1-.5 2.1L8 9.8a16 16 0 0 0 6 6l1.3-1.3a2 2 0 0 1 2.1-.4c.9.3 1.8.6 2.7.7a2 2 0 0 1 1.7 2z"/></svg>555-014-2290</div>
  <div class="info"><svg width="16" height="16" viewBox="0 0 24 24" fill="none" stroke="#e0651e" stroke-width="2"><rect x="2" y="2" width="20" height="20" rx="5"/><path d="M12 7v5l3 2"/></svg><span>Monday - Friday: 8am - 5pm<br>Saturday - Sunday: 8am-12</span></div>
</div>

<div class="abs field" style="left:544px;top:2352px;width:258px;height:39px">First name</div>
<div class="abs field" style="left:818px;top:2352px;width:259px;height:39px">Last name</div>
<div class="abs field" style="left:544px;top:2406px;width:258px;height:39px">Phone number</div>
<div class="abs field" style="left:818px;top:2406px;width:259px;height:39px">Email</div>
<div class="abs field" style="left:544px;top:2467px;width:533px;height:85px">Message</div>
<div class="abs btn" style="left:544px;top:2585px;width:533px;height:38px;background:var(--purple-light);font-family:Inter,sans-serif;font-weight:500;font-size:13.5px">Request submit now</div>

<div class="abs footer"></div>
<div class="abs brand" style="left:109px;top:2826px;color:var(--white);font-size:19px"><i style="background:var(--orange);width:20px;height:20px"></i>Dr Clara Bennett</div>

<div class="abs foot-h" style="left:370px;top:2822px">Contact</div>
<div class="abs" style="left:372px;top:2858px;display:flex;flex-direction:column;gap:6px">
  <div class="info fi"><svg width="16" height="14" viewBox="0 0 16 14" fill="none" stroke="#fff" stroke-width="1.4"><rect x="1" y="1" width="14" height="12" rx="2"/><path d="M1 3l7 5 7-5"/></svg>hello@brightleafcare.com</div>
  <div class="info fi"><svg width="16" height="14" viewBox="0 0 24 24" fill="none" stroke="#fff" stroke-width="2"><path d="M22 16.9v3a2 2 0 0 1-2.2 2 19.8 19.8 0 0 1-8.6-3.1 19.5 19.5 0 0 1-6-6A19.8 19.8 0 0 1 2.1 4.2 2 2 0 0 1 4.1 2h3a2 2 0 0 1 2 1.7c.1.9.4 1.8.7 2.7a2 2 0 0 1-.5 2.1L8 9.8a16 16 0 0 0 6 6l1.3-1.3a2 2 0 0 1 2.1-.4c.9.3 1.8.6 2.7.7a2 2 0 0 1 1.7 2z"/></svg>555-014-2290</div>
  <div class="info fi"><svg width="16" height="16" viewBox="0 0 24 24" fill="none" stroke="#fff" stroke-width="2"><rect x="2" y="2" width="20" height="20" rx="5"/><path d="M12 7v5l3 2"/></svg><span>Monday - Friday: 8am - 5pm<br>Saturday - Sunday: 8am-12</span></div>
</div>

<div class="abs foot-h" style="left:683px;top:2819px">Useful links:</div>
<div class="abs foot-link" style="left:684px;top:2857px">About us</div>
<div class="abs foot-link" style="left:684px;top:2887px">Our services</div>
<div class="abs foot-link" style="left:684px;top:2917px">Fees and information</div>
<div class="abs foot-link" style="left:684px;top:2947px">Contact us</div>

<div class="abs social" style="left:971px;top:2827px"><i></i><i></i><i></i><i></i><i></i></div>

<div class="abs foot-bottom">Copyright © 2010-2024 Lumen Studio S.L. All rights reserved.</div>

</body>
</html>
```